Web Design Project

Please take a look at my current aged website www.tarlowpeopleadvisory.com and my newly designed logo and business cards. I would like a new fresh updated look to my website and my new designs incorporated.
Updates

  Good Morning Everyone

Due to an Austrralian licencing issue I have had to have my logo slightly redesigned.

Would you please be able to look at the newly uploaded files and revise your designs.

Thanks so much.  I am very happy with the calibre and quality of the designs so far.

kind Regards

Marnie

Industry/Entity Type

Business

Requirements
Must have
• the exisiting pages and fresh new graphics and a real commitment to my palette of lime green, turqouise and black.

```html
<!DOCTYPE html>
<html lang="en">
<head>
<meta charset="utf-8">
<title>Tarlow People Advisory</title>
<link href="https://fonts.googleapis.com/css2?family=Ubuntu:wght@400;500;700&family=Arimo:wght@400;700&family=Open+Sans:wght@400;600;700&display=swap" rel="stylesheet">
<style>
:root{
  --lime:#6cc644;
  --lime-dark:#4fa62a;
  --lime-light:#8ee05e;
  --turq:#1aa9c9;
  --turq-dark:#0f8fb0;
  --turq-light:#3fc3dd;
  --ink:#2b2b2b;
  --text:#555;
  --grey:#f3f3f3;
  --line:#cfcfcf;
  --white:#fff;
}
*{margin:0;padding:0;box-sizing:border-box}
html,body{width:928px;height:1200px;overflow:hidden}
body{background:linear-gradient(#84dc58,#5fb637);font-family:Arimo,Arial,sans-serif;color:var(--text);position:relative}
.abs{position:absolute}
.page{left:44px;top:4px;width:840px;height:1128px;background:var(--grey);border-radius:18px}

/* header */
.brand{left:55px;top:28px;display:flex;align-items:center;gap:8px}
.brand-mark{width:64px;height:64px;border-radius:50%;border:4px solid var(--turq)}
.brand-name{font-family:Ubuntu,sans-serif;font-weight:500;font-size:25px;color:var(--turq);letter-spacing:-.3px;white-space:nowrap}
.social-top{left:794px;top:15px;display:flex;gap:9px}
.social-top span{width:20px;height:20px;border-radius:50%;background:radial-gradient(circle at 40% 35%,#4fd0ea,var(--turq-dark));box-shadow:0 2px 2px rgba(0,0,0,.25)}
.call{right:45px;top:46px;font-family:Ubuntu,sans-serif;font-size:17px;color:#888;white-space:nowrap}
.call b{color:var(--turq);font-weight:700;margin-right:4px}
.nav{left:440px;top:85px;display:flex;gap:6px}
.nav a{position:relative;display:block;height:27px;line-height:27px;padding:0;white-space:nowrap;border-radius:7px 7px 3px 3px;background:linear-gradient(var(--turq-light),var(--turq-dark));color:#fff;font-family:"Open Sans",sans-serif;font-size:11px;text-decoration:none;text-align:center}
.nav a::after{content:"";position:absolute;left:50%;bottom:-6px;margin-left:-6px;border:6px solid transparent;border-bottom:0;border-top-color:var(--turq-dark)}
.nav a.current{background:linear-gradient(var(--lime-light),var(--lime-dark))}
.nav a.current::after{border-top-color:var(--lime-dark)}

/* hero */
.hero{left:53px;top:129px;width:824px;height:291px;border-radius:8px;overflow:hidden;background:linear-gradient(160deg,var(--turq-light),var(--turq-dark));border:2px solid #ddd}
.hero-photo{position:absolute;left:0;top:0}
.hero-copy{left:449px;top:20px;width:340px;color:#fff}
.hero-copy h1{font-family:Ubuntu,sans-serif;font-weight:700;font-size:20px;line-height:25px;letter-spacing:.3px;white-space:nowrap}
.hero-copy p{font-size:11px;line-height:17px;margin:10px 0 0 5px}
.hero-list{list-style:none;margin:13px 0 0 11px;font-size:11px;line-height:20px}
.hero-list li{display:flex;align-items:center;gap:7px}
.btn-more{left:459px;top:239px;width:117px;height:35px;border-radius:18px;border:2px solid #fff;background:linear-gradient(var(--lime-light),var(--lime-dark));color:#fff;font-family:Ubuntu,sans-serif;font-weight:700;font-size:14px;line-height:31px;text-align:center}
.pager{left:677px;top:258px;display:flex;gap:5px}
.pager span{width:13px;height:13px;background:#fff;color:var(--turq);font:700 9px/13px Arimo,sans-serif;text-align:center}
.pager span.on{background:var(--lime);color:#fff}

/* intro */
.h2{font-family:Ubuntu,sans-serif;font-weight:700;font-size:17px;color:#333;white-space:nowrap}
.h2 em{font-style:normal;color:var(--turq)}
.intro-title{left:67px;top:447px}
.dotted{left:66px;top:474px;width:368px;border-top:1px dotted #999}
.intro-photo{left:62px;top:512px;width:150px;height:118px;transform:rotate(-13deg);background:linear-gradient(135deg,#e9eef2,#9fb3c2 60%,#3a4a5a);border:5px solid #fff;box-shadow:0 2px 6px rgba(0,0,0,.25)}
.intro-text{left:236px;top:496px;width:334px;font-size:10.5px;line-height:17px}
.tick-list{list-style:none;font-size:11px;line-height:20px;color:#555}
.tick-list li{display:flex;align-items:center;gap:8px}
.intro-list{left:249px;top:560px}
.shadow-rule{left:59px;top:670px;width:510px;height:6px;background:radial-gradient(ellipse at center top,rgba(0,0,0,.18),transparent 70%)}

/* services */
.services-title{left:60px;top:693px;color:var(--turq)}
.services-title span{color:#333}
.services-rule{left:59px;top:721px;width:447px;border-top:1px solid #aaa}
.lead{left:61px;top:743px;font-size:13.5px;color:#222;white-space:nowrap}
.services-icon{left:62px;top:772px;width:35px;height:52px;border-radius:4px;background:linear-gradient(90deg,#777 50%,var(--turq) 50%)}
.services-text{left:111px;top:776px;width:459px;font-size:10.5px;line-height:17px;text-align:justify}
.dot-list{left:66px;top:838px;list-style:none;font-size:10px;color:var(--turq-dark)}
.dot-list li{height:25.5px;display:flex;align-items:center;gap:9px;white-space:nowrap}
.dot-list li::before{content:"";width:4px;height:4px;border-radius:50%;background:var(--lime)}

/* testimonial */
.testimonial{left:616px;top:447px;width:255px;height:165px;border-radius:14px;background:linear-gradient(#fff,#ececec);box-shadow:0 1px 3px rgba(0,0,0,.15)}
.testi-icon{left:11px;top:0;width:42px;height:38px;border-radius:50%;background:radial-gradient(circle at 40% 40%,#7fd6f0,var(--turq) 60%,var(--lime))}
.testi-title{left:56px;top:13px;color:var(--turq)}
.testi-title span{color:#333}
.testi-text{left:22px;top:49px;width:224px;font-size:10.5px;line-height:18.5px;text-align:justify}
.quote{font-family:Georgia,serif;font-size:22px;color:#777;font-weight:700}

/* form */
.consult{left:620px;top:634px;width:243px;height:279px;border-radius:10px;background:linear-gradient(#fff,#ececec);box-shadow:0 1px 3px rgba(0,0,0,.12)}
.consult-title{left:60px;top:15px;color:var(--turq-dark)}
.consult-title span{color:var(--turq-dark)}
.consult-icon{left:17px;top:14px}
.field{position:absolute;left:0;width:230px;display:flex;align-items:center}
.field label{width:67px;text-align:right;padding-right:7px;font-family:"Open Sans",sans-serif;font-size:9px;color:#444;white-space:nowrap}
.field span{width:156px;height:21px;border-radius:7px;background:#fff;border:1px solid #ddd;box-shadow:inset 0 1px 2px rgba(0,0,0,.08)}
.field.tall{align-items:flex-start}
.field.tall span{height:51px}
.submit{left:117px;top:251px;width:99px;height:35px;background:linear-gradient(var(--turq-light),var(--turq-dark));color:#fff;font-family:Ubuntu,sans-serif;font-weight:700;font-size:13px;line-height:35px;text-align:center}
.submit::before,.submit::after{content:"";position:absolute;bottom:-5px;border-top:5px solid var(--turq-dark)}
.submit::before{left:-7px;border-left:7px solid transparent}
.submit::after{right:-7px;border-right:7px solid transparent}

/* footer panel */
.foot{left:55px;top:941px;width:816px;height:174px;background:#fff;border:1px solid #e2e2e2}
.source{left:17px;top:8px;font-family:"Open Sans",sans-serif;font-size:13.5px;line-height:17px;color:var(--turq-dark)}
.book{left:12px;top:49px;width:237px;height:112px;border:6px solid #333;background:linear-gradient(90deg,#f4f4f4,#d8d8d8 45%,#b34a4a 70%,#eee)}
.foot h3{position:absolute;font-family:"Open Sans",sans-serif;font-weight:400;font-size:18.5px;color:#444;letter-spacing:.6px}
.contact-h{left:320px;top:14px}
.principal{left:319px;top:61px;font-family:"Open Sans",sans-serif;font-weight:700;font-size:10.5px;color:#333}
.address{left:321px;top:85px;font-family:"Open Sans",sans-serif;font-size:10.5px;line-height:17px;color:#444}
.address b{color:#333}
.follow-h{left:581px;top:14px}
.follow-box{left:577px;top:49px;width:205px;height:50px;border-radius:10px;border:1px solid #ddd;display:flex;align-items:center;justify-content:center;gap:5px;box-shadow:0 1px 3px rgba(0,0,0,.1)}
.follow-box span{width:27px;height:27px;border-radius:4px;background:linear-gradient(var(--turq-light),var(--turq-dark))}
.follow-box span:nth-child(even){background:linear-gradient(#555,#222)}
.follow-box span:last-child{border-radius:50%;background:linear-gradient(var(--lime-light),var(--lime-dark))}
.links{left:586px;top:106px;font-family:"Open Sans",sans-serif;font-size:10.5px;line-height:20px;color:#444;white-space:nowrap}
.links a{color:var(--lime-dark);text-decoration:none}
.links i{font-style:normal;display:inline-block;width:37px}

/* bottom */
.bottom-nav{left:0;width:928px;top:1147px;text-align:center;font-family:"Open Sans",sans-serif;font-size:11px;color:#fff}
.bottom-nav a{color:#fff;text-decoration:none;margin:0 9px}
.copyright{left:0;width:928px;top:1168px;text-align:center;font-size:11px;color:#fff}
</style>
</head>
<body>
<div class="abs page"></div>

<header>
  <div class="abs brand"><span class="brand-mark"></span><span class="brand-name">Tarlow People Advisory</span></div>
  <div class="abs social-top" aria-label="Social profiles"><span></span><span></span><span></span></div>
  <div class="abs call"><b>Call Us :</b>+0412 555 019</div>
  <nav class="abs nav">
    <a class="current" style="width:68px">Home</a>
    <a style="width:89px">Our Services</a>
    <a style="width:107px">Our Consultants</a>
    <a style="width:74px">Our Fees</a>
    <a style="width:80px">Contact us</a>
  </nav>
</header>

<section class="abs hero">
  <svg class="hero-photo" width="824" height="291" viewBox="0 0 824 291">
    <defs>
      <linearGradient id="photoTone" x1="0" y1="0" x2="1" y2="1">
        <stop offset="0" stop-color="#eef1f2"/>
        <stop offset=".5" stop-color="#c9cfd3"/>
        <stop offset="1" stop-color="#3a3f46"/>
      </linearGradient>
    </defs>
    <path role="img" aria-label="Photo of two smiling business professionals in an office" d="M0 0H420Q500 120 515 291H0Z" fill="url(#photoTone)"/>
    <path d="M420 0Q500 120 515 291" fill="none" stroke="#fff" stroke-width="3" opacity=".8"/>
  </svg>
  <div class="abs hero-copy">
    <h1>Outsourced Human Resources<br>Solution and Stategies</h1>
    <p>Tarlow People Advisory are an outsourced HR function.&nbsp; We can provide you with that ongoing support, offer solutions and assist you with developing strategies that fit your business and deliver results.</p>
    <ul class="hero-list">
      <li><svg width="11" height="10"><path d="M1 5l3 3 6-7" fill="none" stroke="#fff" stroke-width="2.2"/></svg>People Systems and Processes</li>
      <li><svg width="11" height="10"><path d="M1 5l3 3 6-7" fill="none" stroke="#fff" stroke-width="2.2"/></svg>Employee Relations</li>
      <li><svg width="11" height="10"><path d="M1 5l3 3 6-7" fill="none" stroke="#fff" stroke-width="2.2"/></svg>Organisation Development</li>
    </ul>
  </div>
  <div class="abs btn-more">Readmore</div>
  <div class="abs pager"><span>&lsaquo;</span><span class="on">1</span><span>2</span><span>3</span><span>4</span><span>5</span><span>&rsaquo;</span></div>
</section>

<section>
  <h2 class="abs h2 intro-title">What can <em>Tarlow People Advisory</em> do for me?</h2>
  <div class="abs dotted"></div>
  <div class="abs intro-photo" role="img" aria-label="Photo card of a businessman beside a consulting services meeting room"></div>
  <p class="abs intro-text">Tarlow People Advisory are an outsourced HR function.&nbsp; We can provide you with that ongoing support, offer solutions and assist you with developing strategies that fit your business and deliver results.</p>
  <ul class="abs tick-list intro-list">
    <li><svg width="12" height="11"><path d="M1 6l3.5 3.5L11 1" fill="none" stroke="#1aa9c9" stroke-width="2.4"/></svg>People Systems and Processes</li>
    <li><svg width="12" height="11"><path d="M1 6l3.5 3.5L11 1" fill="none" stroke="#1aa9c9" stroke-width="2.4"/></svg>Employee Relations</li>
    <li><svg width="12" height="11"><path d="M1 6l3.5 3.5L11 1" fill="none" stroke="#1aa9c9" stroke-width="2.4"/></svg>Organisation Development</li>
  </ul>
  <div class="abs shadow-rule"></div>
</section>

<section>
  <h2 class="abs h2 services-title"><em>Our</em> <span>Services</span>
    <svg width="26" height="14" style="margin-left:10px;vertical-align:-1px"><path d="M1 7h18M14 2l6 5-6 5" fill="none" stroke="#777" stroke-width="1.6" stroke-dasharray="2 2"/></svg></h2>
  <div class="abs services-rule"></div>
  <p class="abs lead">Lorem Ipsum is simply dummy text of the printing and typesetting industry.</p>
  <div class="abs services-icon" role="img" aria-label="Illustration of two people sheltering under an umbrella"></div>
  <p class="abs services-text">During these challenging economic times it can be difficult to justify internal human resources management services or support. However as a business owner or Manager you may find that HR support or advice is required from time to time.</p>
  <ul class="abs dot-list">
    <li>Lorem ipsum dolor sit amet, consectetur adipiscing elit.</li>
    <li>Sed at eros velit, euismod bibendum sapien.</li>
    <li>In vehicula turpis ac enim laoreet dapibus luctus libero ultricies.</li>
  </ul>
</section>

<aside class="abs testimonial">
  <div class="abs testi-icon" role="img" aria-label="Illustration of two chatting figures"></div>
  <h2 class="abs h2 testi-title">Our <span>Testimonial</span></h2>
  <span class="abs quote" style="left:6px;top:48px">&ldquo;</span>
  <p class="abs testi-text">Tarlow People Advisory are an outsourced HR function.&nbsp; We can provide you with that ongoing support, offer solutions and assist you with developing strategies that fit your business and deliver results.</p>
  <span class="abs quote" style="left:112px;top:136px">&rdquo;</span>
</aside>

<aside class="abs consult">
  <svg class="abs consult-icon" width="36" height="32" viewBox="0 0 36 32">
    <path d="M14 3h19v14h-9l-5 5v-5h-5z" fill="#fff" stroke="#d33" stroke-width="2"/>
    <path d="M2 10h17v13H9l-5 5v-5H2z" fill="#fff" stroke="#1a8fc9" stroke-width="2"/>
  </svg>
  <h2 class="abs h2 consult-title">Free <span>Consultation</span></h2>
  <div class="field" style="top:58px"><label>Your Name:</label><span></span></div>
  <div class="field" style="top:90px"><label>Telephone:</label><span></span></div>
  <div class="field" style="top:122px"><label>Email:</label><span></span></div>
  <div class="field" style="top:154px"><label>Zip Code :</label><span></span></div>
  <div class="field tall" style="top:186px"><label style="padding-top:4px">Comments :</label><span></span></div>
  <div class="abs submit">Submit Now</div>
</aside>

<footer class="abs foot">
  <p class="abs source">Source:&nbsp; The Practical Handbook of Smart<br>Outsourcing 2005</p>
  <div class="abs book" role="img" aria-label="Photo of a woman on the phone at a desk with a computer and paperwork"></div>
  <h3 class="contact-h">Contact Us</h3>
  <p class="abs principal">Principal Consultant MARNIE TARLOW</p>
  <p class="abs address">48b Carrow Street<br>Westmere&nbsp; WA&nbsp; 6021<br><b>Mobile :</b>&nbsp; 0412 555 019</p>
  <h3 class="follow-h">Follow us!</h3>
  <div class="abs follow-box" aria-label="Social profiles"><span></span><span></span><span></span><span></span><span></span><span></span></div>
  <p class="abs links"><i>Email</i>: <a>marnie@tarlowpeopleadvisory.com</a><br><i>Web</i>: <a>www.tarlowpeopleadvisory.com</a></p>
</footer>

<nav class="abs bottom-nav"><a>Home</a>|<a>Our Services</a>|<a>Our Consultants</a>|<a>Our Fees</a>|<a>Contact us</a></nav>
<p class="abs copyright">Copyright &copy; 2011 Tarlow People Advisory All Rights Reserved.</p>
</body>
</html>
```